Round box die line design of photo-realistic prescription medicine bottle

We sell unique products for drinking enthusiasts and we’re in search of a designer to collaborate with us on gag designs for our round gift boxes for wine and booze bottles.

Our initial product will be designed to look like a pharmacy pill bottle with a prescription sticker. I’ve included examples of the pill bottles as well as the “prescription.”

I’ve also attached a picture of an existing paper tube for wine as it’s probably easier to see an actual image than trying to picture it from my terrible description.

This design needs to cover the entire paper tube approximately 13.5 inches by 7.5 inches

Thank you in advance for taking the time to look at my project request. Please feel free to reach out with any questions.

Target Market(s)

The life of the party

Industry/Entity Type

ecommerce

Colors
EE7325
F08F49
F5BC92
FAE3D3
FDF4ED

Requirements
Must have
• Look at realistic as possible
Should not have
• a label design just uploaded to an existing 3d template

```html
<!DOCTYPE html>
<html lang="en">
<head>
<meta charset="utf-8">
<title>Prescription Strength Wine – Tube Wrap</title>
<link rel="stylesheet" href="https://fonts.googleapis.com/css2?family=Roboto+Mono:wght@400;500;700&display=swap">
<style>
  :root {
    --page: #ffffff;
    --cap-light: #eeebeb;
    --cap-mid: #dcd7d7;
    --cap-band-top: #bdb8b8;
    --cap-band: #dedada;
    --orange-main: #f7a823;
    --orange-band: #f08a2a;
    --label: #ffffff;
    --ink: #161616;
    --yellow: #f5e400;
    --rx-orange: #ee7325;
    --seal-red: #d2232a;
    --frame: #1d1d1d;
  }
  * { margin: 0; padding: 0; box-sizing: border-box; }
  html, body {
    width: 1200px; height: 559px; overflow: hidden;
    background: var(--page);
  }
  .wrap {
    position: absolute; left: 130px; top: 18px;
    width: 940px; height: 522px;
    background: var(--orange-main);
    border: 1px solid var(--frame);
    overflow: hidden;
    font-family: "Roboto Mono", monospace;
    color: var(--ink);
  }
  .cap-grip {
    position: absolute; left: 0; top: 0; width: 100%; height: 74px;
    background: linear-gradient(var(--cap-light) 0%, var(--cap-mid) 55%, var(--cap-light) 100%);
  }
  .cap-band {
    position: absolute; left: 0; top: 74px; width: 100%; height: 20px;
    background: linear-gradient(var(--cap-band-top) 0 35%, var(--cap-band) 35% 100%);
  }
  .shoulder-band {
    position: absolute; left: 0; top: 94px; width: 100%; height: 14px;
    background: var(--orange-band);
  }
  .base-band {
    position: absolute; left: 0; bottom: 0; width: 100%; height: 38px;
    background: var(--orange-band);
  }
  .label {
    position: absolute; left: 332px; top: 135px;
    width: 275px; height: 325px;
    background: var(--label);
    border-radius: 22px;
  }
  .label > * { position: absolute; }
  .rx-mark {
    left: 38px; top: 19px; width: 38px; height: 63px;
    background: var(--rx-orange);
    border-radius: 10px 10px 4px 4px;
  }
  .strength { left: 88px; top: 17px; font-size: 12px; letter-spacing: 0.2px; white-space: nowrap; }
  .product {
    left: 85px; top: 22px; font-size: 60px; font-weight: 700;
    line-height: 1; letter-spacing: -1px;
    transform: scaleY(1.05); transform-origin: top left;
  }
  .bar { left: 28px; background: var(--yellow); }
  .bar-main { top: 90px; width: 220px; height: 12px; }
  .bar-thin { top: 132px; width: 220px; height: 4px; }
  .bar-end { top: 276px; width: 192px; height: 4px; }
  .meta { left: 27px; font-size: 10px; font-weight: 700; line-height: 12.6px; white-space: nowrap; }
  .meta-rx { top: 104px; }
  .for { left: 27px; top: 138px; font-size: 20px; font-weight: 700; line-height: 1; }
  .directions {
    left: 28px; top: 162px; width: 219px; height: 58px;
    border: 1px solid var(--rx-orange);
    padding: 2px 4px;
    font-size: 9.3px; line-height: 12.6px; white-space: nowrap;
  }
  .warning { left: 28px; top: 224px; font-size: 9.3px; line-height: 12.6px; white-space: nowrap; }
  .warning-title { font-weight: 700; }
  .refills { left: 28px; top: 285px; font-size: 9.3px; font-weight: 700; line-height: 12.6px; white-space: nowrap; }
  .seal {
    position: absolute; left: 556px; top: 392px;
    width: 80px; height: 80px;
  }
</style>
</head>
<body>
  <main class="wrap" aria-label="Prescription Strength Wine tube wrap, 13.5 by 7.5 inches">
    <div class="cap-grip" role="img" aria-label="Ribbed white bottle cap grip"></div>
    <div class="cap-band"></div>
    <div class="shoulder-band"></div>
    <div class="base-band"></div>

    <section class="label">
      <div class="rx-mark" role="img" aria-label="Orange Rx wine glass emblem"></div>
      <p class="strength">PRESCRIPTION STRENGTH</p>
      <h1 class="product">WINE</h1>
      <div class="bar bar-main"></div>
      <p class="meta meta-rx">RX #: VINO-NECTOR<br>DR. FEEL GOOD</p>
      <div class="bar bar-thin"></div>
      <h2 class="for">FOR:</h2>
      <p class="directions">TAKE 2-6 OZ BY MOUTH TO RELIEVE<br>STRESS, END BAD DAYS, AND FORGET<br>THE HATERS. REPEAT AS NEEDED OR<br>UNTIL BOTTLE IS EMPTY.</p>
      <p class="warning"><span class="warning-title">WARNING:</span><br>SIDE EFFECTS COULD INCLUDE SILLINESS,<br>LOTS OF LAUGHTER AND FORGETTING OF<br>LIFE’S STRESSES.</p>
      <div class="bar bar-end"></div>
      <p class="refills">REFILLS: YES!<br>EXPIRES: WHEN EMPTY</p>
    </section>

    <svg class="seal" viewBox="0 0 80 80" aria-hidden="true">
      <circle cx="40" cy="40" r="37" fill="#ffffff" stroke="var(--seal-red)" stroke-width="2.5"/>
      <circle cx="40" cy="40" r="28" fill="none" stroke="var(--seal-red)" stroke-width="1.2"/>
    </svg>
  </main>
</body>
</html>
```